Business card design based on existing website

Please make a business card that is consistent with the look and feel of my new website: http://brindleworth.com.sg. By going to the site, I think you'll have all you need in terms of the work I do and the colors I use.

I would like to ask the winner of this project to then do a separate project to design my stationery.

Target Market(s)

Heads of human resources, people wanting psychotherapy, and executives wanting coaching. (It's quite a mix!)

Industry/Entity Type

Psychology

Contact Information for Business Card

Email: pax5678@brindleworth.com.sg
Website: http://brindleworth.com.sg
Tel: +65 94706152

(I will not have a physical address on the card)

Font styles to use
Serif

Colors

Designer to choose colors to be used in the design.

Requirements
Must have
• On the Front
• ==========
• Have "Dr. Everett Brindleworth" using the font of the website.
• Also "Executive Coach, Psychotherapist, Leadership Professor"
• The back should mention
• ==================
• My degrees
• -------------
• "PhD Kelvale; Post Doc Duncliffe". E.g., "Everett Brindleworth (PhD Kelvale; Post Doc Duncliffe)" where the text between brackets was in smaller font.
• My work
• ----------
• "Executive coach, psychotherapist, and leadership professor"
• My job titles
• ---------------
• "Principal (Brindleworth Consulting)
• Adjunct Professor (Orchid Crest University)
• Adjunct Associate Professor (Meridian Strait University)
• Coach & Supervisor (VORELT) '
• Options:
• 1) you can abbreviate Adjunct Professor to "Adj Prof" or "Adj Professor"; and "Adjunct Associate Professor" to "Adj Assoc Prof"
• 2) you abbreviate "Meridian Strait University" and "Orchid Crest University" to "MSU" and "OCU"
• 3) You can also combine the titles for MSU and OCU, e.g., "Adjunct faculty (MSU & OCU)
Nice to have
• Because I work with many Chinese people, it is sometimes helpful to have my family name, "Brindleworth", in caps. In the past I have not used caps because it takes away from the aesthetic of the card. Only use caps if it looks good.
• The uploaded image of a "EB" is something that may be helpful. I am undecided.
• THANK YOU for helping me!
Should not have
• No photos. In my industry people consider it overselling.

```html
<!DOCTYPE html>
<html lang="en">
<head>
<meta charset="utf-8">
<title>Dr. Everett Brindleworth — Business Card</title>
<link href="https://fonts.googleapis.com/css2?family=EB+Garamond:wght@400;500&family=Oswald:wght@500&family=Open+Sans:wght@400&display=swap" rel="stylesheet">
<style>
  :root {
    --backdrop: #d9d9d7;
    --forest: #1b3220;
    --cream: #ecebc2;
    --paper: #f7f7f6;
    --ink: #1e1e1e;
    --ink-soft: #3a3a3a;
  }
  * { margin: 0; padding: 0; box-sizing: border-box; }
  html, body { width: 1200px; height: 904px; overflow: hidden; }
  body {
    background: var(--backdrop);
    position: relative;
    font-family: "Open Sans", sans-serif;
  }
  .card {
    position: absolute;
    width: 580px;
    height: 330px;
    box-shadow: 0 6px 18px rgba(0,0,0,0.18);
  }
  .card-front {
    left: 250px; top: 70px;
    background: var(--forest);
    display: flex; align-items: center; justify-content: center;
  }
  .front-name {
    font-family: "EB Garamond", serif;
    font-weight: 500;
    font-size: 34px;
    letter-spacing: 0.5px;
    color: var(--cream);
  }
  .card-back {
    left: 370px; top: 500px;
    background: var(--paper);
  }
  .identity {
    position: absolute;
    right: 318px; top: 112px;
    text-align: right;
  }
  .identity-name {
    font-family: "Oswald", sans-serif;
    font-weight: 500;
    font-size: 24px;
    line-height: 1;
    color: var(--forest);
    letter-spacing: 0.2px;
  }
  .identity-degrees {
    font-size: 11px;
    color: var(--ink-soft);
    margin-top: 4px;
  }
  .divider {
    position: absolute;
    left: 280px; top: 88px;
    width: 1.5px; height: 84px;
    background: var(--ink);
  }
  .contacts {
    position: absolute;
    left: 298px; top: 88px;
    list-style: none;
  }
  .contacts li {
    display: flex; align-items: center; gap: 10px;
    font-size: 14px; line-height: 26px;
    color: var(--ink);
  }
  .contacts svg { width: 14px; height: 14px; flex: none; }
  .services {
    position: absolute;
    left: 0; right: 0; bottom: 46px;
    text-align: center;
    font-size: 16px;
    color: var(--ink);
  }
</style>
</head>
<body>
  <section class="card card-front">
    <h1 class="front-name">Dr. Everett Brindleworth</h1>
  </section>

  <section class="card card-back">
    <div class="identity">
      <div class="identity-name">DR. EVERETT BRINDLEWORTH</div>
      <div class="identity-degrees">PhD Kelvale; Post Doc Duncliffe</div>
    </div>
    <div class="divider"></div>
    <ul class="contacts">
      <li>
        <svg viewBox="0 0 14 14" aria-hidden="true"><circle cx="7" cy="7" r="6.5" fill="none" stroke="#1e1e1e" stroke-width="1"/><path d="M4.5 4 l1.5-.5 1 2-1 .8 a4 4 0 0 0 1.8 1.8 l.8-1 2 1-.5 1.5 c-3 .3-6-2.7-5.6-5.6z" fill="#1e1e1e"/></svg>
        +65 94706152
      </li>
      <li>
        <svg viewBox="0 0 14 14" aria-hidden="true"><circle cx="7" cy="7" r="6.5" fill="none" stroke="#1e1e1e" stroke-width="1"/><rect x="3.5" y="4.8" width="7" height="4.6" fill="#1e1e1e"/><path d="M3.5 4.8 L7 7.6 L10.5 4.8" fill="none" stroke="#f7f7f6" stroke-width="0.8"/></svg>
        pax5678@brindleworth.com.sg
      </li>
      <li>
        <svg viewBox="0 0 14 14" aria-hidden="true"><circle cx="7" cy="7" r="6.5" fill="#1e1e1e"/><circle cx="7" cy="7" r="4" fill="none" stroke="#f7f7f6" stroke-width="0.8"/><ellipse cx="7" cy="7" rx="1.7" ry="4" fill="none" stroke="#f7f7f6" stroke-width="0.8"/><path d="M3 7 H11" stroke="#f7f7f6" stroke-width="0.8"/></svg>
        www.brindleworth.com.sg
      </li>
    </ul>
    <p class="services">Executive Coaching | Psychotherapy | Leadership Training</p>
  </section>
</body>
</html>
```